Virtual Assistant/Online Marketing Business Card/Stationary

I need a professional but modern business card/stationary for my company in Dallas called BrivoLane. BrivoLane is a virtual assistant specializing in online marketing. I would like a unique design that stands out and makes my brand clear. Incorporating the logo is a must and have attached it to this brief.

Target Market(s)

small business owners & entrepreneurs, 35-65

Industry/Entity Type

Business

Contact Information for Business Card

Dorla Finch
dorlafinch@brivolane.biz
(214) 555-0187
brivolane.biz

Font styles to use
Sans Serif

Colors
f04a50
3176b5
9bcb3c

Requirements
Must have
• Colors that match the logo colors. Logo integration

```html
<!DOCTYPE html>
<html lang="en">
<head>
<meta charset="utf-8">
<title>BrivoLane Business Card</title>
<link href="https://fonts.googleapis.com/css2?family=Open+Sans:wght@400;600;700&display=swap" rel="stylesheet">
<style>
  :root {
    --page-bg: #d9d6d3;
    --card-bg: #0b0b0b;
    --accent-red: #e0533a;
    --brand-red: #f04a50;
    --brand-blue: #3176b5;
    --brand-green: #9bcb3c;
    --text-light: #f2f2f2;
    --silver: #b9b9b9;
    --divider: #3a2a26;
  }
  * { box-sizing: border-box; margin: 0; padding: 0; }
  html, body {
    width: 1200px;
    height: 900px;
    overflow: hidden;
    background: var(--page-bg);
    font-family: "Open Sans", sans-serif;
  }
  .stage {
    width: 1200px;
    height: 900px;
    display: flex;
    align-items: center;
    justify-content: center;
    gap: 40px;
  }
  .card {
    width: 540px;
    height: 309px;
    background: var(--card-bg);
    border-radius: 4px;
    box-shadow: 0 10px 28px rgba(0,0,0,0.28);
    position: relative;
    overflow: hidden;
  }
  /* Front */
  .card-front { display: flex; }
  .brand-block {
    width: 52%;
    display: flex;
    align-items: flex-end;
    padding: 0 24px 72px 32px;
  }
  .brand-name {
    font-weight: 700;
    font-size: 36px;
    color: var(--text-light);
    letter-spacing: -0.5px;
    line-height: 1;
    white-space: nowrap;
    display: flex;
    align-items: center;
    gap: 10px;
  }
  .brand-dot {
    width: 12px;
    height: 12px;
    border-radius: 50%;
    background: var(--brand-red);
    flex: none;
  }
  .divider {
    position: absolute;
    left: 52%;
    top: 60px;
    width: 1px;
    height: 150px;
    background: var(--divider);
  }
  .contact-block {
    width: 48%;
    padding: 70px 0 0 26px;
  }
  .person-name {
    color: var(--accent-red);
    font-weight: 600;
    font-size: 18px;
    margin-bottom: 20px;
  }
  .contact-list { list-style: none; }
  .contact-item {
    display: flex;
    align-items: center;
    gap: 10px;
    color: var(--text-light);
    font-size: 13px;
    line-height: 1;
    margin-bottom: 9px;
    white-space: nowrap;
  }
  .contact-icon { width: 11px; height: 11px; flex: none; }
  /* Back */
  .card-back {
    display: flex;
    align-items: center;
    justify-content: center;
  }
  .back-brand {
    font-weight: 700;
    font-size: 60px;
    color: var(--silver);
    letter-spacing: -1px;
    white-space: nowrap;
    display: flex;
    align-items: center;
    gap: 16px;
  }
  .back-brand .brand-dot { width: 18px; height: 18px; background: var(--silver); }
</style>
</head>
<body>
<main class="stage">
  <section class="card card-front">
    <div class="brand-block">
      <div class="brand-name"><span class="brand-dot"></span>BrivoLane</div>
    </div>
    <div class="divider"></div>
    <div class="contact-block">
      <h1 class="person-name">Dorla Finch</h1>
      <ul class="contact-list">
        <li class="contact-item">
          <svg class="contact-icon" viewBox="0 0 12 12"><path fill="#e0533a" d="M2.5 1 4.3 1 5 3.6 3.8 4.6A6.5 6.5 0 0 0 7.4 8.2L8.4 7 11 7.7V9.5C11 10.3 10.3 11 9.5 11 5 11 1 7 1 2.5 1 1.7 1.7 1 2.5 1Z"/></svg>
          (214) 555-0187
        </li>
        <li class="contact-item">
          <svg class="contact-icon" viewBox="0 0 12 12"><rect x="1" y="2.5" width="10" height="7" fill="#e0533a"/><path d="M1 2.5 6 6.5 11 2.5" stroke="#0b0b0b" stroke-width="1" fill="none"/></svg>
          dorlafinch@brivolane.biz
        </li>
        <li class="contact-item">
          <svg class="contact-icon" viewBox="0 0 12 12"><circle cx="6" cy="6" r="5" fill="#e0533a"/><path d="M1 6H11M6 1C3.5 4 3.5 8 6 11M6 1C8.5 4 8.5 8 6 11" stroke="#0b0b0b" stroke-width="0.8" fill="none"/></svg>
          www.brivolane.biz
        </li>
      </ul>
    </div>
  </section>
  <section class="card card-back">
    <div class="back-brand"><span class="brand-dot"></span>BrivoLane</div>
  </section>
</main>
</body>
</html>
```